Prepared Meal Company Needs Menu Design

We are a pre-prepared meal delivery company called Greel Brantwick.

We have a menu in excel but needs to be designed to look good and appealing to customers. The menu should be clean, easy to ready, and show:Title (Pupusa)Tags (V, V+, GF - Use a cool vegan logo for the V+ and logo for vegetarian V symbol)Price (12.99)DescriptionBrand colors are orange white and green. Design is clean, crisp and can incorporate natural elements like leaf shaped symbols, etc. Screenshots from our website attached for inspiration.

Target Market(s)

Broad demographics

Industry/Entity Type

Restaurant

Font styles to use
Sans Serif

Requirements
Must have
• The menu design should be commensurate with the website under development
• https://greelbrantwick.tavlorix.com
Nice to have
• Should have appropriate graphics
Should not have
• Modifiers do not need to be shown (these are shown in the excel only).

```html
<!DOCTYPE html>
<html lang="en">
<head>
<meta charset="utf-8">
<title>Greel Brantwick – Snacks / Sides</title>
<link href="https://fonts.googleapis.com/css2?family=Dancing+Script:wght@400;700&family=Oswald:wght@500&display=swap" rel="stylesheet">
<style>
  :root {
    --backdrop: #333333;
    --paper: #fafafa;
    --brand-orange: #f26a21;
    --brand-green: #2f8a3c;
    --ink: #262626;
    --leaf-light: #cfe3b0;
    --leaf-mid: #9fcb83;
    --leaf-deep: #6fae68;
  }
  * { margin: 0; padding: 0; box-sizing: border-box; }
  html, body { width: 1200px; height: 1200px; overflow: hidden; background: var(--backdrop); }
  .menu-page {
    position: absolute; left: 195px; top: 25px; width: 812px; height: 1150px;
    background: var(--paper); overflow: hidden;
  }
  .foliage { position: absolute; opacity: .85; }
  .foliage--left { left: 0; top: 220px; width: 50px; height: 380px;
    background: linear-gradient(90deg, var(--leaf-mid), rgba(207,227,176,0)); border-radius: 0 60% 60% 0; }
  .foliage--left-low { left: 0; top: 820px; width: 40px; height: 330px;
    background: linear-gradient(90deg, var(--leaf-mid), rgba(207,227,176,0)); border-radius: 0 60% 60% 0; }
  .foliage--top-right { left: 700px; top: 210px; width: 112px; height: 200px;
    background: radial-gradient(circle at 70% 50%, var(--leaf-mid), rgba(207,227,176,0) 75%); }
  .foliage--right { left: 690px; top: 430px; width: 122px; height: 720px;
    background: radial-gradient(ellipse at 80% 50%, var(--leaf-mid), var(--leaf-light) 55%, rgba(207,227,176,0) 80%); }
  .foliage--bottom { left: 295px; top: 790px; width: 300px; height: 360px;
    background: radial-gradient(ellipse at 55% 60%, var(--leaf-deep), var(--leaf-light) 55%, rgba(207,227,176,0) 78%); }

  .section-banner { position: absolute; left: 17px; top: 22px; width: 366px; height: 55px; }
  .section-banner svg { position: absolute; inset: 0; }
  .section-banner h1 {
    position: relative; text-align: center; line-height: 55px; color: #fff;
    font: 500 22px/55px 'Oswald', sans-serif; letter-spacing: .5px;
  }

  .menu-column { position: absolute; width: 382px; }
  .menu-column--left { left: 12px; top: 89px; }
  .menu-column--right { left: 417px; top: 17px; }

  .item-head {
    display: flex; align-items: baseline;
    font: 700 15px/21.4px 'Dancing Script', cursive; color: var(--brand-green);
  }
  .item-name { white-space: nowrap; }
  .item-leader { flex: 1; border-bottom: 1px dotted var(--brand-green); margin: 0 6px; transform: translateY(-4px); }
  .item-price { white-space: nowrap; color: var(--brand-green); }
  .item-desc { font: 400 14px/21.4px 'Dancing Script', cursive; color: var(--ink); position: relative; }
  .item-head, .item-desc { position: relative; }
</style>
</head>
<body>
<main class="menu-page">
  <div class="foliage foliage--left" role="img" aria-label="Leafy greens illustration at the left edge"></div>
  <div class="foliage foliage--left-low" role="img" aria-label="Leafy greens illustration at the lower left edge"></div>
  <div class="foliage foliage--top-right" role="img" aria-label="Asparagus and kale illustration"></div>
  <div class="foliage foliage--right" role="img" aria-label="Kale leaves illustration along the right edge"></div>
  <div class="foliage foliage--bottom" role="img" aria-label="Kale and asparagus illustration"></div>

  <header class="section-banner">
    <svg viewBox="0 0 366 55" width="366" height="55" aria-hidden="true">
      <polygon points="0,0 366,0 350,27.5 366,55 0,55 16,27.5" fill="var(--brand-orange)"/>
    </svg>
    <h1>SNACKS / SIDES</h1>
  </header>

  <section class="menu-column menu-column--left">
    <div class="item"><p class="item-head"><span class="item-name">Salmon BurgerSalmon Burger</span><span class="item-leader"></span><span class="item-price">5.99$</span></p><p class="item-desc">Dried Cranberries, Raw Honey, Black Sesame Seeds<br>&amp; Kestrel Sea Salt</p></div>
    <div class="item"><p class="item-head"><span class="item-name">6" Corn Tortilla (V+, GF)</span><span class="item-leader"></span><span class="item-price">1.49$</span></p><p class="item-desc">Handmade Corn Tortillas</p></div>
    <div class="item"><p class="item-head"><span class="item-name">Polenta Cake (V, GF, Dairy Free) [V+ No Honey]</span><span class="item-leader"></span><span class="item-price">3.99$</span></p><p class="item-desc">Hollowbrook Farms Lavender Honey, Rosemary, Sea Salt</p></div>
    <div class="item"><p class="item-head"><span class="item-name">Handmade Gluten-Free Flatbread (V, GF)</span><span class="item-leader"></span><span class="item-price">4.99$</span></p><p class="item-desc">&nbsp;Garden Herb Oil, Sumac, Pistacho &amp; Thyme</p></div>
    <div class="item"><p class="item-head"><span class="item-name">Guacamole (V+, GF)</span><span class="item-leader"></span><span class="item-price">4.99$</span></p><p class="item-desc">Chilaca Chile, Red Onion, Jalapeno, Tomato,<br>Cilantro, Lime &amp; Kestrel Sea Salt</p></div>
    <div class="item"><p class="item-head"><span class="item-name">Soft Yolk Egg (V, GF, Dairy Free)</span><span class="item-leader"></span><span class="item-price">4.99$</span></p><p class="item-desc">Whole Sous Vide Egg</p></div>
    <div class="item"><p class="item-head"><span class="item-name">Ayocote Beans (V+, GF)</span><span class="item-leader"></span><span class="item-price">6.99$</span></p><p class="item-desc">Vado Verde Heirloom Oaxacan Beans w/ Aromatics<br>&amp; Epazote</p></div>
    <div class="item"><p class="item-head"><span class="item-name">Moroccan Red Lentil &amp; Sorghum Patty (V+, GF)</span><span class="item-leader"></span><span class="item-price">4.99$</span></p><p class="item-desc">Red Lentils, Sorghum, Carrots, Onions, Bell Pepper,<br>Guajillo Chile, Cumin, Cardamom, Coriander &amp; Clove</p></div>
    <div class="item"><p class="item-head"><span class="item-name">Wren's Grilled Chicken (GF, Dairy Free)</span><span class="item-leader"></span><span class="item-price">4.99$</span></p><p class="item-desc">Free Range Chicken Breast in Rosemary, Oregano &amp;<br>Thyme Marinade</p></div>
    <div class="item"><p class="item-head"><span class="item-name">Free Range Turkey Meatballs (GF, Dairy Free)</span><span class="item-leader"></span><span class="item-price">4.99$</span></p><p class="item-desc">Free Range Chicken Breast in Rosemary, Oregano &amp;<br>Thyme Marinade</p></div>
    <div class="item"><p class="item-head"><span class="item-name">Pacific Ocean Perch Filet (GF, Dairy Free)</span><span class="item-leader"></span><span class="item-price">6.99$</span></p><p class="item-desc">Pan Seared Pacific Ocean Perch Filet</p></div>
    <div class="item"><p class="item-head"><span class="item-name">Salmon Patty (Dairy Free)</span><span class="item-leader"></span><span class="item-price">6.99$</span></p><p class="item-desc">Scottish Salmon, Spinach &amp; Lemon</p></div>
    <div class="item"><p class="item-head"><span class="item-name">Salmon Filet (GF, Dairy Free)</span><span class="item-leader"></span><span class="item-price">7.99$</span></p><p class="item-desc">Pan Seared Filet of Scottish Salmon</p></div>
    <div class="item"><p class="item-head"><span class="item-name">Tropical Acai Hot Sauce [V+, GF]</span><span class="item-leader"></span><span class="item-price">2.49$</span></p><p class="item-desc">Pomegranate, Strawberry, Guajillo, Jalapeno &amp; Lime</p></div>
    <div class="item"><p class="item-head"><span class="item-name">Chayote Escabeche (V+, GF)</span><span class="item-leader"></span><span class="item-price">2.49$</span></p><p class="item-desc">Chayote Squash, Jalapeno, Extra Virgin Olive Oil &amp; Lemon</p></div>
    <div class="item"><p class="item-head"><span class="item-name">Goat Cheese (V, GF)</span><span class="item-leader"></span><span class="item-price">2.99$</span></p><p class="item-desc">Chayote Squash, Jalapeno, Extra Virgin Olive Oil &amp; Lemon</p></div>
    <div class="item"><p class="item-head"><span class="item-name">Monkfruit &amp; Balsamic Glaze (V+, GF)</span><span class="item-leader"></span><span class="item-price">2.99$</span></p><p class="item-desc">Balsamic Vinager sweetened &amp; reduced with Monkfruit.</p></div>
    <div class="item"><p class="item-head"><span class="item-name">Salsa Roja (V+, GF)</span><span class="item-leader"></span><span class="item-price">1.29$</span></p><p class="item-desc">Guajillo, Ancho &amp; Tomato.</p></div>
    <div class="item"><p class="item-head"><span class="item-name">Manzanilla Yogurt (V, GF)</span><span class="item-leader"></span><span class="item-price">1.39$</span></p><p class="item-desc">Greek Yogurt with Honey, Roman Chamomile &amp; Lemon</p></div>
    <div class="item"><p class="item-head"><span class="item-name">Cilantro-Lime Yogurt (V, GF)</span><span class="item-leader"></span><span class="item-price">1.39$</span></p><p class="item-desc">Greek Yogurt with Cilantro, Lime, Honey &amp; Cumin.</p></div>
    <div class="item"><p class="item-head"><span class="item-name">Saffron &amp; Chamomile Yogurt (V, GF)</span><span class="item-leader"></span><span class="item-price">1.99$</span></p><p class="item-desc">Greek Yogurt with Saffron, Chamomile, Honey &amp; Citrus.</p></div>
  </section>

  <section class="menu-column menu-column--right">
    <div class="item"><p class="item-head"><span class="item-name">Cider Vinaigrette (V, GF, Dairy Free)</span><span class="item-leader"></span><span class="item-price">2.29$</span></p><p class="item-desc">Arbequina Olive Oil, Apple Cider Vinager &amp; Raw Honey</p></div>
    <div class="item"><p class="item-head"><span class="item-name">Carrot-Ginger Vinaigrette (V, GF, Dairy Free)</span><span class="item-leader"></span><span class="item-price">1.39$</span></p><p class="item-desc">Raw Honey, Carrot, Ginger, Olive Oil &amp; Vinager</p></div>
    <div class="item"><p class="item-head"><span class="item-name">Solano Grove Arbequina Extra Virgin</span></p><p class="item-head"><span class="item-name">Olive Oil (V+, GF)</span><span class="item-leader"></span><span class="item-price">1.99$</span></p><p class="item-desc">Solano Grove Arbequina Extra Virgin Olive Oil</p></div>
    <div class="item"><p class="item-head"><span class="item-name">Lemon Juice (V+, GF)</span><span class="item-leader"></span><span class="item-price">0.75$</span></p><p class="item-desc">Marrowell Lemon Juice</p></div>
    <div class="item"><p class="item-head"><span class="item-name">Lime Juice (V+, GF)</span><span class="item-leader"></span><span class="item-price">0.75$</span></p><p class="item-desc">Marrowell Lemon Juice</p></div>
    <div class="item"><p class="item-head"><span class="item-name">Almond Butter (V+, GF)</span><span class="item-leader"></span><span class="item-price">4.49$</span></p><p class="item-desc">Marrowell Lemon Juice</p></div>
    <div class="item"><p class="item-head"><span class="item-name">Raw Wildflower Honey (V, GF, Dairy Free)</span><span class="item-leader"></span><span class="item-price">2.99$</span></p><p class="item-desc">California Raw Wildflower Honey</p></div>
    <div class="item"><p class="item-head"><span class="item-name">Coco Cream (V+, GF)</span><span class="item-leader"></span><span class="item-price">2.99$</span></p><p class="item-desc">Vegan Coconut Whipped Cream</p></div>
  </section>
</main>
</body>
</html>
```